Fore Sale sign for my real estate agency

I am a Brisbane - Australia inner western suburbs boutique real estate agent who is needing a for sale sign. We are a small dynamic family agency that needs a for sale sign that will standout and give us a strong presence in the market.

I have attached a logo I like, however I am not fixed on anything and am open to suggestions.

The information on the sign should contain but not necessarily limited to the following information - please appreciate I am very open
1 logo - Vellman
2 Ph number - 3847 1593
3 web address - vellman.example.au

Thank you
Glen Vellman

```html
<!DOCTYPE html>
<html lang="en">
<head>
<meta charset="utf-8">
<title>Vellman Real Estate – For Sale Sign</title>
<link rel="stylesheet" href="https://fonts.googleapis.com/css2?family=Montserrat:wght@600;700;800&display=swap">
<style>
  :root {
    --backdrop: #e9e9e7;
    --sign-white: #f7f7f5;
    --brand-orange: #e0620f;
    --brand-black: #1d1b1c;
    --text-dark: #1d1b1c;
    --text-light: #ffffff;
  }
  * { margin: 0; padding: 0; box-sizing: border-box; }
  html, body {
    width: 1200px;
    height: 900px;
    overflow: hidden;
    background: var(--backdrop);
    font-family: "Montserrat", Arial, sans-serif;
  }
  .canvas {
    width: 1200px;
    height: 900px;
    display: flex;
    align-items: center;
    justify-content: center;
  }
  .sale-sign {
    width: 880px;
    height: 725px;
    display: flex;
    flex-direction: column;
    box-shadow: 0 6px 24px rgba(0,0,0,0.18);
  }
  .sign-brand {
    height: 284px;
    background: var(--sign-white);
    display: flex;
    flex-direction: column;
    align-items: center;
    justify-content: center;
    padding-top: 10px;
  }
  .brand-name {
    font-weight: 700;
    font-size: 118px;
    line-height: 1;
    letter-spacing: -3px;
    color: var(--text-dark);
  }
  .brand-tagline {
    margin-top: 8px;
    font-weight: 800;
    font-size: 40px;
    letter-spacing: 1px;
    color: var(--brand-orange);
  }
  .sign-headline {
    height: 232px;
    background: var(--brand-orange);
    display: flex;
    align-items: center;
    justify-content: center;
  }
  .headline-text {
    font-weight: 800;
    font-size: 146px;
    line-height: 1;
    letter-spacing: -4px;
    color: var(--text-light);
  }
  .sign-phone {
    height: 147px;
    background: var(--brand-black);
    display: flex;
    align-items: center;
    justify-content: center;
  }
  .phone-number {
    font-weight: 700;
    font-size: 100px;
    line-height: 1;
    letter-spacing: 2px;
    color: var(--text-light);
  }
  .sign-web {
    height: 62px;
    background: var(--sign-white);
    display: flex;
    align-items: center;
    justify-content: center;
  }
  .web-address {
    font-weight: 700;
    font-size: 30px;
    color: var(--text-dark);
  }
</style>
</head>
<body>
  <main class="canvas">
    <section class="sale-sign" aria-label="Vellman Real Estate for sale sign">
      <header class="sign-brand">
        <div class="brand-name">Vellman</div>
        <div class="brand-tagline">REAL ESTATE</div>
      </header>
      <div class="sign-headline">
        <h1 class="headline-text">FOR SALE</h1>
      </div>
      <div class="sign-phone">
        <p class="phone-number">3847 1593</p>
      </div>
      <footer class="sign-web">
        <p class="web-address">www.vellman.example.au</p>
      </footer>
    </section>
  </main>
</body>
</html>
```